Modern Design for Eyecare business - Vision Center, Optometry, Eye Doctors, Health Care

Create a sleek, modern, sharp homepage design for a eyecare center in Oklahoma City, OK. The vision center provides eyecare health services along with prescription eyewear.

I have included the logo which should be the basis of the designs look and feel. No other imagery was given so feel free to include stock photos and illustrations that you believe give the design a fresh look.

Please do not include stock photos of people/humans

I have included a document that provides some verbiage for the design as well as the designs main navigation.

They have an existing website http://www.bluepineoptics.example/ but are not happy with it. The new design should be different than their existing design.

List of websites for inspiration:
http://www.harborfaith.example
https://www.meadowlenspartners.example
http://www.brightsmiledental.example/
https://www.keltro.example

Target Market(s)

all ages

industry: Health, Eyewear, Eyecare, Optometry

Industry/Entity Type

Health

Number of Pages Required

1 page

Requirements
Must have
• Light color scheme that matches logo colors.
• Sophisticated, sleek design that resembles the logo's style.
Nice to have
• Large, full width visual banner with a 'contact us, etc' call-to-action between header and homepage content
Should not have
• No stock images of people/humans.
• Other forms of stock photos/illustrations are fine.

```html
<!DOCTYPE html>
<html lang="en">
<head>
<meta charset="utf-8">
<title>Bluepine Optics – Opening Your Eyes To Clearer Vision</title>
<link href="https://fonts.googleapis.com/css2?family=Lato:wght@300;400;700&family=Raleway:wght@300;400;600&display=swap" rel="stylesheet">
<style>
:root{
  --blue:#55a6f4;
  --blue-dark:#3f8fe0;
  --blue-text:#4a9be8;
  --slate:#4a5663;
  --slate-deep:#2f3944;
  --ink:#3c4650;
  --muted:#6f7a86;
  --line:#dde3ea;
  --night:#1b1d24;
  --white:#ffffff;
}
*{margin:0;padding:0;box-sizing:border-box}
html,body{width:1200px;height:3030px;overflow:hidden}
body{font-family:"Lato",sans-serif;color:var(--ink);background:var(--white);position:relative}
.section{position:absolute;left:0;width:1200px}
.abs{position:absolute}

/* Hero */
.hero{top:0;height:489px;background:linear-gradient(180deg,#5a6672 0%,#46525e 60%,#3b4650 100%);overflow:hidden}
.hero-backdrop{position:absolute;inset:0;background:radial-gradient(circle at 870px 150px,rgba(255,255,255,.18),transparent 260px),radial-gradient(circle at 150px 260px,rgba(255,255,255,.1),transparent 220px)}
.brand{left:126px;top:28px;display:flex;align-items:center;gap:10px;color:var(--white);font-family:"Raleway",sans-serif;font-size:20px;font-weight:400}
.brand-dot{width:14px;height:14px;border-radius:50%;background:var(--white)}
.nav{right:58px;top:32px;display:flex;gap:10px;list-style:none}
.nav li{font-size:10.5px;font-weight:700;color:var(--white);padding:7px 12px;border-radius:14px}
.nav li.active{background:var(--blue)}
.hero-title{top:122px;width:100%;text-align:center;color:var(--white);font-family:"Raleway",sans-serif;font-weight:300;font-size:21px}
.hero-title strong{font-weight:600}
.hero-actions{top:166px;width:100%;display:flex;justify-content:center;gap:20px}
.btn{font-size:10px;font-weight:700;letter-spacing:.3px;text-transform:uppercase;color:var(--white);width:138px;height:37px;display:flex;align-items:center;justify-content:center}
.btn-solid{background:var(--blue)}
.btn-ghost{border:1.5px solid var(--white)}
.screen{left:376px;top:228px;width:336px;height:270px;background:#1e2228;border-radius:10px 10px 0 0;padding:12px}
.screen-media{width:100%;height:100%;background:linear-gradient(135deg,#eef0f2,#c9ced4 60%,#8f969e);display:flex;align-items:center;justify-content:center;gap:10px}
.play{width:40px;height:40px;border-radius:50%;background:rgba(30,34,40,.75);display:flex;align-items:center;justify-content:center}
.watch{font-size:13px;font-weight:700;color:#1e2228}

/* Subscribe */
.subscribe{top:489px;height:97px;background:var(--blue);color:var(--white)}
.subscribe h2{position:absolute;left:272px;top:22px;font-family:"Lato",sans-serif;font-weight:400;font-size:18px}
.subscribe p{position:absolute;left:272px;top:51px;font-size:10px;opacity:.9}
.email{left:516px;top:27px;width:312px;height:40px;background:var(--blue-dark);display:flex;align-items:center;gap:12px;padding-left:14px;font-size:10.5px;color:rgba(255,255,255,.75)}
.join{left:840px;top:27px;width:126px;height:40px;border:1.5px solid var(--white);display:flex;align-items:center;justify-content:center;gap:8px;font-size:11px;font-weight:700}

/* Features */
.features{top:586px;height:246px}
.feature{position:absolute;top:62px;width:190px;text-align:center}
.feature-icon{width:96px;height:96px;border-radius:50%;background:var(--blue);margin:0 auto;display:flex;align-items:center;justify-content:center}
.feature p{margin-top:20px;font-size:13px;line-height:1.7;color:var(--blue-text)}
.divider{position:absolute;left:0;width:1200px;height:1px;background:var(--line)}
.divider-mark{position:absolute;left:585px;width:30px;height:30px}

/* Sight */
.sight{top:832px;height:346px}
.sight h2{position:absolute;left:196px;top:56px;font-family:"Raleway",sans-serif;font-weight:300;font-size:31px;color:var(--blue-text)}
.sight p{position:absolute;left:196px;top:110px;width:436px;font-size:9.5px;line-height:1.8;color:var(--muted)}
.learn{left:196px;top:230px;width:90px;height:24px;border-radius:12px;background:var(--blue);color:var(--white);font-size:10px;font-weight:700;display:flex;align-items:center;justify-content:center}
.sight-photo{left:713px;top:67px;width:314px;height:210px;background:linear-gradient(135deg,#ffffff,#dfe4ea 50%,#9ea8b3)}

/* Experts */
.experts{top:1178px;height:371px;border-top:1px solid var(--line)}
.experts-photo{left:0;top:0;width:598px;height:371px;background:radial-gradient(ellipse at 50% 60%,#3f8ac0,#16314f 60%,#0b1524)}
.experts-mark{left:582px;width:32px;height:32px;border-radius:50%;background:var(--blue);border:3px solid var(--white)}
.experts h2{position:absolute;left:638px;top:24px;font-family:"Raleway",sans-serif;font-weight:300;font-size:28px;color:var(--blue-text)}
.experts p{position:absolute;left:638px;width:500px;font-size:14px;line-height:1.55;color:var(--ink)}

/* Personalized */
.care{top:1549px;height:309px}
.care h2{position:absolute;top:80px;width:100%;text-align:center;font-family:"Raleway",sans-serif;font-weight:300;font-size:29px;color:var(--blue-text)}
.care p{position:absolute;left:188px;top:142px;width:824px;text-align:center;font-size:13.5px;line-height:1.55;color:var(--ink)}

/* Why us */
.why{top:1858px;height:368px}
.why-panel{left:0;top:0;width:600px;height:368px;background:var(--blue);color:var(--white)}
.why-panel h2{position:absolute;left:40px;top:40px;font-family:"Raleway",sans-serif;font-weight:400;font-size:29px}
.why-list{position:absolute;left:34px;top:88px;width:500px;list-style:none}
.why-list li{position:relative;padding-left:14px;font-size:13.5px;line-height:1.3;margin-bottom:2px}
.why-list li::before{content:"";position:absolute;left:0;top:5px;border-left:7px solid var(--white);border-top:4px solid transparent;border-bottom:4px solid transparent}
.why-photo{left:600px;top:0;width:600px;height:368px;background:linear-gradient(135deg,#f4f5f6,#d7dbdf 55%,#aab1b8)}

/* Map */
.map{top:2226px;height:315px;background:linear-gradient(180deg,#e8eaec,#dfe2e5)}

/* Contact */
.contact{top:2541px;height:412px;background:var(--night);color:var(--white)}
.contact h2{position:absolute;top:52px;width:100%;text-align:center;font-family:"Raleway",sans-serif;font-weight:400;font-size:24px}
.contact-rule{left:560px;top:94px;width:80px;height:2px;background:var(--blue)}
.contact p{position:absolute;left:360px;top:110px;width:480px;text-align:center;font-size:9px;line-height:1.6;color:#b8bec7}
.field{font-size:9.5px;color:#d0d4da;border-bottom:1.5px solid #cfd3d8;padding:0 0 8px 10px}
.send{left:733px;top:323px;width:108px;height:32px;border:1px solid #cfd3d8;font-size:10px;display:flex;align-items:center;justify-content:center}

/* Footer */
.footer{top:2953px;height:77px;background:var(--white)}
.footer-brand{left:48px;top:28px;display:flex;align-items:center;gap:6px;font-family:"Raleway",sans-serif;font-size:13px;color:var(--slate-deep)}
.footer-brand span.dot{width:9px;height:9px;border-radius:50%;background:var(--slate-deep)}
.partner{left:192px;top:20px;width:62px;height:34px;border-radius:50%;background:#cfe3f3}
.copyright{top:34px;width:100%;text-align:center;font-size:10px;color:var(--muted)}
.social{right:58px;top:30px;display:flex;gap:18px}
.social span{width:13px;height:13px;border-radius:50%;background:#6d9bd1}
</style>
</head>
<body>

<header class="section hero">
  <div class="hero-backdrop" role="img" aria-label="Soft-focus background of an eye examination phoropter"></div>
  <div class="abs brand"><span class="brand-dot"></span>Bluepine Optics</div>
  <ul class="abs nav">
    <li class="active">Home</li><li>Vision Services</li><li>Vision Health</li><li>Patient Info</li><li>Patient</li><li>Reviews</li><li>Schedule Appointment</li><li>Contact</li>
  </ul>
  <h1 class="abs hero-title">Opening <strong>Your Eyes</strong> To Clearer Vision</h1>
  <div class="abs hero-actions"><span class="btn btn-solid">Request Appointment</span><span class="btn btn-ghost">Contact Us</span></div>
  <div class="abs screen">
    <div class="screen-media" role="img" aria-label="Video still of eyeglasses resting on an eye chart">
      <span class="play"><svg width="14" height="14" viewBox="0 0 14 14"><path d="M3 1l10 6-10 6z" fill="#fff"/></svg></span>
      <span class="watch">WATCH VIDEO</span>
    </div>
  </div>
</header>

<section class="section subscribe">
  <h2>Subscribe</h2>
  <p>Join our email list to get future update</p>
  <div class="abs email"><svg width="16" height="12" viewBox="0 0 16 12"><rect x=".75" y=".75" width="14.5" height="10.5" fill="none" stroke="#fff" stroke-width="1.2"/><path d="M1 1l7 6 7-6" fill="none" stroke="#fff" stroke-width="1.2"/></svg>Your Email Address</div>
  <div class="abs join">JOIN <svg width="12" height="12" viewBox="0 0 12 12"><path d="M1 6l10-5-3 10-2-4z" fill="none" stroke="#fff" stroke-width="1.2"/></svg></div>
</section>

<section class="section features">
  <div class="feature" style="left:315px">
    <div class="feature-icon"><svg width="46" height="46" viewBox="0 0 46 46" fill="none" stroke="#fff" stroke-width="2.5"><path d="M3 23c6-9 13-13 20-13s14 4 20 13c-6 9-13 13-20 13S9 32 3 23z"/><circle cx="23" cy="23" r="7"/><circle cx="23" cy="23" r="2.5" fill="#fff"/></svg></div>
    <p>Opening Your Eyes To<br>Clearer Vision</p>
  </div>
  <div class="feature" style="left:503px">
    <div class="feature-icon"><svg width="46" height="46" viewBox="0 0 46 46" fill="none" stroke="#fff" stroke-width="2.5"><circle cx="23" cy="23" r="15"/><circle cx="23" cy="23" r="8"/><circle cx="23" cy="23" r="2.5" fill="#fff"/><path d="M23 2v7M23 37v7M2 23h7M37 23h7"/></svg></div>
    <p>A Personalized Approach<br>To Vision Correction</p>
  </div>
  <div class="feature" style="left:689px">
    <div class="feature-icon"><svg width="46" height="46" viewBox="0 0 46 46" fill="none" stroke="#fff" stroke-width="2.5" stroke-linejoin="round"><path d="M12 8h22l9 11-20 21L3 19z"/><path d="M3 19h40M17 8l-4 11 10 21 10-21-4-11"/></svg></div>
    <p>Committed To Excellence<br>In Vision Care</p>
  </div>
  <div class="divider" style="top:242px"></div>
  <svg class="divider-mark" style="top:227px" viewBox="0 0 30 30"><path d="M15 1l13 7v14l-13 7-13-7V8z" fill="#55a6f4"/><path d="M10 13l5 5 5-5" fill="none" stroke="#fff" stroke-width="2"/></svg>
</section>

<section class="section sight">
  <h2>Sight is precious... Don't you think?</h2>
  <p>Our welcoming staff has one common goal – providing you with the best vision care possible and assisting you in finding you the finest eyewear that suits your lifestyle. While many big chain stores employ sales consultants to sell you glasses or contacts, our practice is comprised of knowledgeable individuals whose primary goal is to provide you with a high level of customer service all while ensuring you get the eye care you need and deserve.</p>
  <span class="abs learn">Learn More...</span>
  <div class="abs sight-photo" role="img" aria-label="Close-up of an eye examination slit lamp instrument"></div>
</section>

<section class="section experts">
  <div class="abs experts-photo" role="img" aria-label="Eyeglasses bringing a blurred city at night into focus"></div>
  <span class="abs experts-mark" style="top:73px"></span>
  <span class="abs experts-mark" style="top:160px"></span>
  <span class="abs experts-mark" style="top:247px"></span>
  <h2>True Experts of Eye Care</h2>
  <p style="top:86px">Many people resort to the simple solution of purchasing glasses at a drug store or pharmacy, but it could cost them their vision.</p>
  <p style="top:146px">Our optometrists are skilled at not only detecting typical refractive errors (nearsightedness,farsightedness, and astigmatism) and prescribing the proper corrective eyewear, but also finding eye diseases in their early stages. You can't get that from a convenience store.</p>
  <p style="top:244px">Without regularly scheduled eye examinations, you may not realize that you are suffering from an eye disease until it affects your vision and may be more difficult to treat.</p>
  <div class="divider" style="top:369px"></div>
  <svg class="divider-mark" style="top:354px" viewBox="0 0 30 30"><path d="M15 1l13 7v14l-13 7-13-7V8z" fill="#55a6f4"/><path d="M10 13l5 5 5-5" fill="none" stroke="#fff" stroke-width="2"/></svg>
</section>

<section class="section care">
  <h2>Personalized Patient Care &amp; Treatment</h2>
  <p>Refractive errors and other eye problems are common; however, not all ocular conditions are the same. At our practice, each patient is given a comprehensive eye examination, which allows our optometrist to get the whole picture of your eye health and find potential vision problems. Only after carefully reviewing the findings of your exam, do we offer a treatment plan. If you do have a refractive error and are unsure of your options, our optometrist can help you decide between eyeglasses and contact lenses. We can also discuss the pros and cons of refractive surgery, like LASIK. At our office, we take the time to give you the comprehensive vision treatment that you need and deserve.</p>
</section>

<section class="section why">
  <div class="abs why-panel">
    <h2>Why Us?</h2>
    <ul class="why-list">
      <li>We treat you like a VIP - every experience you have with us will leave you knowing you received the VIP treatment</li>
      <li>We are here to serve YOU - we offer same day appointments and convenient clinic hours and the treatment of eye diseases</li>
      <li>We have the best trained and friendliest staff devoted to your care</li>
      <li>We offer the latest in eye care technology including the Lumora Scan OCT, the Retivue retinal exam, and Clarix high-definition eyeglass lenses</li>
      <li>We are providers for most insurance plans</li>
      <li>We have strong relationships and network with the very best retinal, corneal, cataract, and LASIK surgeons in the state</li>
      <li>We have the Lumora Field which provides the earliest detection of visual field loss</li>
    </ul>
  </div>
  <div class="abs why-photo" role="img" aria-label="Black-framed eyeglasses in front of an eye chart"></div>
</section>

<section class="section map" role="img" aria-label="Street map showing the clinic location"></section>

<section class="section contact">
  <h2>Contact Us</h2>
  <span class="abs contact-rule"></span>
  <p>Send us a note with any question about exams, eyewear or insurance, and a member of our friendly team will reply to you within one business day.</p>
  <div class="abs field" style="left:358px;top:200px;width:232px">Your name here</div>
  <div class="abs field" style="left:606px;top:200px;width:236px">Your mail here</div>
  <div class="abs field" style="left:358px;top:288px;width:484px">Your message here</div>
  <span class="abs send">Send Message</span>
</section>

<footer class="section footer">
  <div class="abs footer-brand"><span class="dot"></span>Bluepine Optics</div>
  <span class="abs partner"></span>
  <p class="abs copyright">Copyright © 2016 Bluepine Optics</p>
  <div class="abs social"><span></span><span></span><span></span><span></span></div>
</footer>

</body>
</html>
```